Ready to be wowed! Snazzy, sassy, classy Realtor seeking Web banner for unique innovative Realtor!

Placer County Realtor need web banner re-design. Looking for classy, classic, clean design appealing to elite prospects. Previous focus was short sales now looking to gear towards listing and selling homes, remove short sale focus. Must include, license # 07354218, HE logo, phone, email, etc. check out MaraVoss.com for reference info. I am open to suggestions for other needed content for THE BEST WEB BANNER ON EARTH! LOL. I really want to appeal to the upscale clients, also will be getting away from orange colors going more to a green. Please contact me at MaraVossSells@postvale.net for more info
measurements of banner; Images of exactly 960 × 120 pixels will be used as-is. It's Wordpress Genesis.

I'm really looking for something clean that looks upscale and luxury, classy. 

Please update email address to mara@maravoss.com

Reason: I still haven't gotten what I want. I noticed some really good designs closer to the end here, I'm hoping to allow those folks and maybe a few new ones the opportunity to give me exactly what I want! Thanks!

Reason: I still don't have what I want. I want a simple design that shows that I am a Realtor, maybe a picture of a house???? or something related to real estate. Less emphasis on the Harrowgate Estates logo. Classy and upscale. Fonts should be easy to read but not so simply boring. Please, please, please read the brief!! I REALLY want a good banner!!

Please take a look at the site color adjustment. That's what color it will stay. www.MaraVoss.com

Reason: I'm ready to move this to the end now. I need a design. I'm extending hopefully only this last time to take a vote on them. I will be reaching out to a few select designers to make a few modifications. I appreciate everyone's time on this as you know this is a very tough and important decision to make.

Reason: Need more input

Reason: still trying to decide

upscale home sellers

Realtor

• License # 07354218
Phone (916)555-0147
HE LOGO (attached)
areas of service- Roseville, Rocklin, Granite Bay
MaraVossSells@postvale.net

```html
<!DOCTYPE html>
<html lang="en">
<head>
<meta charset="utf-8">
<title>Mara Voss – Realtor</title>
<link rel="stylesheet" href="https://fonts.googleapis.com/css2?family=PT+Sans:wght@400;700&family=Great+Vibes&family=Libre+Baskerville&display=swap">
<style>
  :root {
    --page-bg: #2c2b2a;
    --green: #3f7a4a;
    --green-light: #6aa56f;
    --green-deep: #2a5a35;
    --panel-dark: #3a3938;
    --nav-text: #d8d4cf;
    --white: #ffffff;
    --input-text: #b8b2ab;
    --btn-bg: #e6f0d8;
    --btn-text: #1f3324;
    --card-heading: #2e2e2e;
    --brand-square: #233a6b;
  }
  * { box-sizing: border-box; margin: 0; padding: 0; }
  html, body { width: 1200px; height: 375px; overflow: hidden; }
  body {
    background: var(--page-bg);
    font-family: "PT Sans", Arial, sans-serif;
    position: relative;
  }

  /* Header banner */
  .banner {
    position: absolute; left: 56px; top: 0; width: 1088px; height: 136px;
    background: linear-gradient(100deg, var(--green-deep) 0%, var(--green) 35%, var(--green-light) 55%, var(--green) 75%, var(--green-deep) 100%);
  }
  .brand {
    position: absolute; left: 14px; top: 30px; width: 118px; height: 46px;
    display: flex; align-items: center; gap: 6px;
  }
  .brand-mark { width: 14px; height: 14px; background: var(--brand-square); flex: none; }
  .brand-name {
    color: var(--white); font-size: 13px; font-weight: 700; line-height: 1.15;
  }
  .license {
    position: absolute; left: 14px; top: 83px;
    color: var(--white); font-size: 24px;
  }
  .areas, .email {
    position: absolute; left: 149px; color: var(--white);
    font-family: "Libre Baskerville", Georgia, serif;
  }
  .areas { top: 24px; font-size: 14px; }
  .email { top: 59px; font-size: 13px; }
  .phone {
    position: absolute; left: 149px; top: 83px;
    color: var(--white); font-size: 24px;
  }
  .agent-name {
    position: absolute; right: 128px; top: 30px;
    color: var(--white); font-family: "Great Vibes", cursive; font-size: 64px;
    line-height: 1; white-space: nowrap;
  }
  .agent-photo {
    position: absolute; left: 976px; top: 20px; width: 88px; height: 98px;
    border: 2px solid var(--white);
    background: linear-gradient(160deg, #6f8fb0 0%, #c8a27a 55%, #7a5a3e 100%);
  }
  .banner-pointer {
    position: absolute; left: 86px; top: 136px; width: 0; height: 0;
    border-left: 11px solid transparent; border-right: 11px solid transparent;
    border-top: 10px solid var(--green-deep);
  }

  /* Navigation */
  .main-nav {
    position: absolute; left: 78px; top: 166px;
    display: flex; list-style: none;
  }
  .main-nav li {
    color: var(--nav-text); font-size: 14px; text-transform: uppercase;
    margin-right: 45px;
  }
  .main-nav li.current { color: var(--white); font-weight: 700; }

  /* Newsletter band */
  .newsletter {
    position: absolute; left: 56px; top: 214px; width: 1088px; height: 113px;
    background: var(--green);
  }
  .newsletter-arrow { position: absolute; left: 0; top: 0; }
  .newsletter-title {
    position: absolute; left: 24px; top: 18px;
    color: var(--white); font-size: 24px; font-weight: 700; letter-spacing: 0.3px;
  }
  .newsletter-text {
    position: absolute; left: 24px; top: 53px; width: 570px;
    color: #c9c4bf; font-size: 13px; line-height: 1.6;
  }
  .email-field {
    position: absolute; left: 689px; top: 35px; width: 290px; height: 46px;
    background: var(--white); border: 1px solid #c6dcc4;
    display: flex; align-items: center; padding-left: 18px; gap: 22px;
    color: var(--input-text); font-size: 13px; font-weight: 700; letter-spacing: 0.6px;
  }
  .go-button {
    position: absolute; left: 996px; top: 35px; width: 56px; height: 44px;
    background: var(--btn-bg); border-radius: 3px;
    display: flex; align-items: center; justify-content: center;
    color: var(--btn-text); font-size: 16px; font-weight: 700;
  }

  /* Feature cards */
  .card {
    position: absolute; top: 329px; height: 60px; background: var(--white);
    text-align: center; padding-top: 33px;
    color: var(--card-heading); font-size: 24px; font-weight: 700; text-transform: uppercase;
    white-space: nowrap; overflow: hidden;
  }
  .card-sell { left: 56px; width: 358px; }
  .card-video { left: 420px; width: 360px; }
  .card-indicators { left: 787px; width: 357px; }
</style>
</head>
<body>
  <header class="banner">
    <div class="brand"><span class="brand-mark"></span><span class="brand-name">Harrowgate Estates</span></div>
    <div class="license">#07354218</div>
    <div class="areas">Roseville, Rocklin, Granite Bay</div>
    <div class="email">MaraVossSells@postvale.net</div>
    <div class="phone">(916)555-0147</div>
    <div class="agent-name">Mara Voss</div>
    <div class="agent-photo" role="img" aria-label="Portrait photo of the realtor"></div>
  </header>
  <div class="banner-pointer"></div>

  <ul class="main-nav">
    <li class="current">Home</li>
    <li>About</li>
    <li>Home Buyers</li>
    <li>Home Sellers</li>
    <li>Testimonials</li>
    <li>Contact</li>
  </ul>

  <section class="newsletter">
    <svg class="newsletter-arrow" width="604" height="113" viewBox="0 0 604 113">
      <polygon points="0,0 550,0 604,56 550,113 0,113" fill="#1f1e1d"/>
      <polygon points="0,0 538,0 590,56 538,113 0,113" fill="#3a3938"/>
    </svg>
    <h2 class="newsletter-title">REAL ESTATE NEWS &amp; RESOURCES</h2>
    <p class="newsletter-text">Join our readers who receive regular market updates, trends, and Roseville &amp; Rocklin Real estate resources, directly to their inbox...FREE. Don't miss out! Enter your email to the right.</p>
    <div class="email-field">
      <svg width="16" height="11" viewBox="0 0 16 11"><rect x="0.5" y="0.5" width="15" height="10" fill="none" stroke="#c9c4bf"/><polyline points="0.5,0.5 8,6 15.5,0.5" fill="none" stroke="#c9c4bf"/></svg>
      ENTER YOUR EMAIL ADDRESS...
    </div>
    <div class="go-button">GO</div>
  </section>

  <div class="card card-sell">Sell My House - Show</div>
  <div class="card card-video">Educational Video</div>
  <div class="card card-indicators">12 Indicators You May</div>
</body>
</html>
```